FAST TURNAROUND - simple sound/yoga event postcard

If you are up for a fast turnaround project within the next few hours then please submit your ideas. I have a photo, the text and a drawing of my idea for the front of the postcard.
PLEASE! Don't submit designs unless you are available now and can go back and forth to complete this project quickly -thank you-
PLEASE READ DETAILS FIRST - some designers are asking questions about things that I have outlined and specified in the brief -PLEASE LOOK AT ALL THE FILES - I have a doc about my ideas for the FRONT that are specific- thanks

FRONT OF THE POST CARD:
Please do not put anything else on the front other than the text on my instruction doc
I would like the lettering on the front of the card to be white or black (or white with black border) with simple fonts. However, I'm open to seeing the words VELVET LANTERN in color blue for contrast
OPTION #1 for placing the title Velvet Lantern is to have the letter inside the gong (see my ideas for the front uploaded doc)
OPTION #2 for placing the title VELVET LANTERN is the upper left part of the postcard.
lettering for lower left is Sound + Yogic Sleep (yoga nidra)

BACK OF THE POSTCARD:
BLACK BACKGROUND with white lettering. would love to see a couple of ideas of how you think the layout might look. I am open to only my website address being in blue as a contrast (or any of the other text) I've uploaded my logo but only on back side please keep it small
THANK YOU!

Target Market(s)

Yoga Students

Industry/Entity Type

Event

Requirements
Must have
• Must be 4.25 X 6.25 with bleed line CMYK - 300dpi PDF that follows the printers template (see uploaded files)
PLEASE READ INSTRUCTIONS ABOVE

Simple design please
Nice to have
• SEE ABOVE
Should not have
• LOGO NOT ON FRONT OF CARD
NO COLOR ON FRONT OF CARD JUST B AND W - maybe Velvet Lantern in color blue only

```html
<!DOCTYPE html>
<html lang="en">
<head>
<meta charset="utf-8">
<title>Velvet Lantern – Postcard</title>
<link rel="stylesheet" href="https://fonts.googleapis.com/css2?family=Cormorant+Garamond:wght@500&family=Source+Sans+3:wght@400;700&display=swap">
<style>
  :root {
    --backdrop: #8c8c8c;
    --paper: #ffffff;
    --ink: #111111;
    --night: #000000;
    --snow: #ffffff;
    --link-blue: #2b3f7f;
    --link-blue-light: #4a7fc1;
    --accent-orange: #e87a1e;
    --gong-dark: #1e1e1e;
    --gong-mid: #5a5a5a;
    --gong-halo: #cfcfcf;
  }
  * { margin: 0; padding: 0; box-sizing: border-box; }
  html, body { width: 1161px; height: 1200px; overflow: hidden; }
  body {
    position: relative;
    background: var(--backdrop);
    font-family: "Source Sans 3", "Myriad Pro", sans-serif;
  }

  /* Front card */
  .card-front {
    position: absolute; left: 120px; top: 50px; width: 681px; height: 528px;
    background: var(--paper); color: var(--ink); text-align: center;
  }
  .front-title {
    position: absolute; left: 0; right: 0; top: 30px; padding-left: 12px;
    font-family: "Cormorant Garamond", "Times New Roman", serif;
    font-weight: 500; font-size: 51px; letter-spacing: 0.5px; line-height: 1;
  }
  .front-subtitle {
    position: absolute; left: 0; right: 0; top: 82px; font-size: 15px;
  }
  .gong-art {
    position: absolute; left: 164px; top: 100px; width: 356px; height: 356px;
    border-radius: 50%;
    background: radial-gradient(circle at 50% 50%, var(--gong-mid) 0 6%, var(--gong-dark) 14% 42%, var(--gong-mid) 45%, var(--gong-dark) 47%, var(--gong-halo) 50%, #ececec 62%, var(--paper) 72%);
  }
  .front-credit {
    position: absolute; left: 0; right: 0; top: 439px;
    font-size: 14.5px; line-height: 18.5px; letter-spacing: 0.2px;
  }
  .front-link { color: var(--link-blue); }

  /* Back card */
  .card-back {
    position: absolute; left: 327px; top: 614px; width: 681px; height: 528px;
    background: var(--night); color: var(--snow);
  }
  .back-intro {
    position: absolute; left: 0; right: 0; top: 38px;
    text-align: center; font-size: 18px; line-height: 22.3px; letter-spacing: 0.6px;
  }
  .back-intro p + p { margin-top: 22.3px; }
  .brand-mark {
    position: absolute; left: 0; right: 0; top: 262px;
    display: flex; justify-content: center; align-items: center; gap: 6px;
    font-size: 14px; color: var(--accent-orange);
  }
  .brand-dot { width: 12px; height: 12px; border-radius: 50%; background: var(--accent-orange); }
  .schedule { position: absolute; top: 306px; font-size: 17px; }
  .schedule-left { left: 52px; }
  .schedule-right { left: 404px; top: 304px; }
  .schedule h2 { font-size: 21px; font-weight: 700; margin-bottom: 7px; }
  .schedule-left h2 { letter-spacing: 0.3px; }
  .venue { line-height: 18px; }
  .venue-city { display: block; font-size: 11px; line-height: 12px; margin-bottom: 9px; }
  .schedule li { list-style: none; line-height: 29px; }
  .back-link {
    position: absolute; left: 0; right: 0; top: 480px;
    text-align: center; font-size: 14.5px; color: var(--link-blue-light);
  }
</style>
</head>
<body>
  <section class="card-front">
    <h1 class="front-title">VELVET LANTERN</h1>
    <p class="front-subtitle">Tone, Breath and Resonance Healing Program</p>
    <div class="gong-art" role="img" aria-label="Photograph of a dark planetary gong surrounded by a swirl of grey music notes"></div>
    <p class="front-credit">
      Maren Solace is certified in Sound Healing through the Tone, Breath and Resonance Healing Program<br>
      of Western Institute of Holistic Arts (WIHA) and a Level III Certified Restwell Yoga Nidra Teacher<br>
      <span class="front-link">For more information: www.marensolace.com</span>
    </p>
  </section>

  <section class="card-back">
    <div class="back-intro">
      <p>Velvet Lantern offers deep relaxation and attunement to well-being<br>through a combination of sound healing with Yoga Nidra<br>(yogic sleep meditation).</p>
      <p>Your sound healing journey will immerse you in the sonic resonance of<br>Planetary Gongs, Tibetan and crystal singing bowls and a variety of sound<br>healing instruments.</p>
      <p>Feel free to bring a pillow, your own blanket or a covering for your eyes!</p>
    </div>

    <div class="brand-mark"><span class="brand-dot"></span>Maren Solace</div>

    <div class="schedule schedule-left">
      <h2>Velvet Lantern dates:</h2>
      <p class="venue">Lotus Grove -Potrero Studio<span class="venue-city">(San Francisco)</span></p>
      <ul>
        <li>February 15, 2015</li>
        <li>May 23rd, 2015</li>
        <li>June 21st, 2015</li>
      </ul>
    </div>

    <div class="schedule schedule-right">
      <h2>Yoga Nidra Workshops:</h2>
      <p class="venue">Lotus Grove-Valencia Studio<span class="venue-city">(San Francisco)</span></p>
      <ul>
        <li>February 15, 2015</li>
        <li>May 23rd, 2015</li>
        <li>June 21st, 2015</li>
      </ul>
    </div>

    <p class="back-link">For more information: www.marensolace.com</p>
  </section>
</body>
</html>
```